BWLK (a church) flyer for our locality to advertise us

A double-sided colour A5 flyer that introduces our church to our local community. It should include our logo, and be sympathetic to its colours. It should say who we are, when we meet and talk about what we do. It needs to show our location and how to get to us, where you can park, and how to contact us.
We want it to look modern, bright and inviting. More information can be found at www.bwlk-example.org and www.lanternnook-example.org and Facebook lantern.nook.uk

A copy of our previous flyer is attached. Our folks thought it was too dull and emphasised the cafe too much.

Target Market(s)

People within our locality in SE London who may be interested in attending our church, or visiting our cafe, Lantern Nook

Industry/Entity Type

Charity

Font styles to use
Sans Serif

Colors
6b449b
876aae
33a6d7
0455a3
fee18a
ffffff

Requirements
Must have
• A description of who we are at BWLK; what we do; what our values are; when & where we meet & how to contact us. Something to draw people in - a magnetic effect. A modern look & feel. A primary emphasis on our church.
Nice to have
• Design that is sympathetic to our logo colours (livery)
Should not have
• Too much emphasis on the Lantern Nook cafe.

```html
<!DOCTYPE html>
<html lang="en">
<head>
<meta charset="utf-8">
<title>BWLK – A Place To Be Loved</title>
<link rel="stylesheet" href="https://fonts.googleapis.com/css2?family=Cinzel:wght@700&family=Dancing+Script:wght@600&family=Lato:wght@400;700&family=Oswald:wght@600&display=swap">
<style>
  :root {
    --purple: #6b449b;
    --lilac: #876aae;
    --blue: #33a6d7;
    --navy: #0455a3;
    --yellow: #fee18a;
    --white: #ffffff;
    --ink: #1f1830;
    --line-dark: #1f1830;
    --cream: #efe6d6;
    --cream-dark: #c2ab88;
    --cocoa: #8c715c;
    --cocoa-light: #d3c2b1;
  }
  html, body {
    margin: 0;
    padding: 0;
    width: 900px;
    height: 1200px;
    overflow: hidden;
    background: var(--white);
  }
  .flyer {
    position: relative;
    width: 900px;
    height: 1200px;
    overflow: hidden;
    font-family: "Lato", sans-serif;
    color: var(--ink);
    background: radial-gradient(ellipse at 50% 45%, #fff6d8 0%, var(--yellow) 70%);
  }
  .flyer--back { display: none; }
  .flyer__shapes {
    position: absolute;
    inset: 0;
  }

  /* ---------- front ---------- */
  .brand {
    position: absolute;
    left: 50px;
    top: 130px;
    display: flex;
    align-items: center;
    gap: 14px;
  }
  .brand__dot {
    width: 26px;
    height: 26px;
    border-radius: 50%;
    background: var(--blue);
  }
  .brand__name {
    font-weight: 700;
    font-size: 52px;
    color: var(--purple);
    letter-spacing: 2px;
  }
  .headline {
    position: absolute;
    right: 62px;
    top: 62px;
    width: 470px;
    text-align: center;
    color: var(--white);
  }
  .headline__name {
    font-family: "Cinzel", serif;
    font-weight: 700;
    font-size: 62px;
    line-height: 1;
    margin: 0;
  }
  .headline__sub {
    font-size: 29px;
    line-height: 1.15;
    margin: 8px 0 0;
    letter-spacing: 0.5px;
  }
  .headline__tag {
    font-family: "Oswald", sans-serif;
    font-weight: 600;
    font-size: 46px;
    line-height: 1.1;
    margin: 4px 0 0;
    letter-spacing: 0.5px;
  }
  .invite {
    position: absolute;
    left: 174px;
    width: 560px;
    top: 458px;
    height: 66px;
    border-top: 2px solid var(--purple);
    border-bottom: 2px solid var(--purple);
    display: flex;
    align-items: center;
    justify-content: center;
    font-family: "Dancing Script", cursive;
    font-weight: 600;
    font-size: 38px;
    color: var(--ink);
  }
  .about {
    position: absolute;
    left: 140px;
    width: 640px;
    top: 552px;
    text-align: center;
    font-size: 20.5px;
    line-height: 1.45;
    margin: 0;
  }
  .meet {
    position: absolute;
    left: 120px;
    width: 500px;
    top: 714px;
    margin: 0;
    text-align: center;
    font-size: 19px;
    line-height: 1.4;
    color: var(--purple);
  }
  .meet strong { font-weight: 700; }
  .drink { position: absolute; }
  .drink--hot {
    left: 628px;
    top: 712px;
    width: 260px;
    height: 260px;
    border-radius: 50%;
    background: radial-gradient(circle at 50% 55%, var(--white) 0%, var(--cream) 35%, var(--cream-dark) 100%);
    box-shadow: 0 0 0 6px var(--white);
  }
  .drink--iced {
    left: -10px;
    top: 940px;
    width: 220px;
    height: 280px;
    border-radius: 0 34px 0 0;
    background: linear-gradient(180deg, var(--cocoa-light) 0%, var(--cocoa) 100%);
    border: 4px solid var(--line-dark);
  }
  .contact {
    position: absolute;
    left: 240px;
    width: 420px;
    top: 878px;
    text-align: center;
    color: var(--white);
    font-size: 20px;
    line-height: 1.33;
    margin: 0;
  }
  .contact__title { font-weight: 700; }

  /* ---------- back ---------- */
  .back__title {
    position: absolute;
    left: 60px;
    top: 70px;
    margin: 0;
    font-family: "Oswald", sans-serif;
    font-weight: 600;
    font-size: 50px;
    color: var(--white);
  }
  .back__grid {
    position: absolute;
    left: 60px;
    top: 330px;
    width: 780px;
    display: grid;
    grid-template-columns: 1fr 1fr;
    gap: 34px 50px;
  }
  .back__block h3 {
    margin: 0 0 8px;
    font-size: 24px;
    color: var(--purple);
  }
  .back__block p {
    margin: 0;
    font-size: 19px;
    line-height: 1.45;
  }
  .back__foot {
    position: absolute;
    left: 60px;
    right: 60px;
    top: 960px;
    text-align: center;
    color: var(--white);
    font-size: 21px;
    line-height: 1.5;
    margin: 0;
  }

  @media print {
    html, body { height: auto; overflow: visible; }
    .flyer--back { display: block; break-before: page; }
  }
</style>
</head>
<body>
<main class="flyer flyer--front">
  <svg class="flyer__shapes" width="900" height="1200" viewBox="0 0 900 1200" aria-hidden="true">
    <defs>
      <linearGradient id="blueBand" x1="0" y1="0" x2="0" y2="1">
        <stop offset="0" stop-color="#33a6d7"/>
        <stop offset="1" stop-color="#0455a3"/>
      </linearGradient>
      <linearGradient id="purpleBand" x1="0" y1="0" x2="1" y2="1">
        <stop offset="0" stop-color="#876aae"/>
        <stop offset="1" stop-color="#6b449b"/>
      </linearGradient>
    </defs>
    <path d="M0,0 H900 V290 Q480,420 0,375 Z" fill="#ffffff"/>
    <path d="M0,368 Q480,410 900,278" fill="none" stroke="#1f1830" stroke-width="12"/>
    <path d="M330,0 H900 V262 Q480,395 0,352 V300 C150,290 250,250 290,150 C310,90 315,40 330,0 Z" fill="url(#purpleBand)"/>
    <path d="M0,0 H330 C315,40 310,90 290,150 C250,250 150,290 0,300 Z" fill="#ffffff"/>
    <path d="M0,888 Q420,808 900,850 V1200 H0 Z" fill="#1f1830"/>
    <path d="M0,900 Q420,822 900,862 V1200 H0 Z" fill="url(#blueBand)"/>
  </svg>

  <div class="brand">
    <span class="brand__dot"></span>
    <span class="brand__name">BWLK</span>
  </div>

  <header class="headline">
    <h1 class="headline__name">BRIGHT WELL</h1>
    <p class="headline__sub">LIVING KINGDOM MINISTRIES</p>
    <p class="headline__tag">A PLACE TO BE LOVED</p>
  </header>

  <div class="invite">we invite you to worship with us</div>

  <p class="about">
    BWLK, a place where everyone is welcome: different ethnicities, ages, social groups, abilities and disabilities, and interests.<br>
    We also have Ladies Group — 1st Friday of every month (informal, informative and lots of fun!) Night vigil — every quarter, please confirm by phone Counselling — by appointment only
  </p>

  <p class="meet">
    <strong>Sunday worship 11.00am</strong> · Wednesday prayer 7.30pm<br>
    14 Example Lane, London SE0 0AA · free parking on site
  </p>

  <div class="drink drink--hot" role="img" aria-label="Photo of a latte with heart-shaped foam art seen from above"></div>
  <div class="drink drink--iced" role="img" aria-label="Photo of an iced chocolate drink in a glass with a straw"></div>

  <p class="contact">
    <span class="contact__title">For further enquiries: Office:</span><br>
    Tuesday through Friday<br>
    10.30am - 3.00pm<br>
    Telephone: INT'l +44 (0)20 3000 0123<br>
    Evenings: INT'L +44(0)20 8000 0456<br>
    E-mail: hello@bwlk-example.org<br>
    Web: www.bwlk-example.org
  </p>
</main>

<section class="flyer flyer--back" aria-label="Back of flyer">
  <svg class="flyer__shapes" width="900" height="1200" viewBox="0 0 900 1200" aria-hidden="true">
    <path d="M0,0 H900 V190 Q480,300 0,250 Z" fill="#6b449b"/>
    <path d="M0,258 Q480,308 900,198" fill="none" stroke="#1f1830" stroke-width="10"/>
    <path d="M0,940 Q420,870 900,905 V1200 H0 Z" fill="#0455a3"/>
  </svg>
  <h2 class="back__title">FIND US &amp; JOIN US</h2>
  <div class="back__grid">
    <div class="back__block"><h3>Who we are</h3><p>BWLK is a friendly local church family in SE London, open to everyone.</p></div>
    <div class="back__block"><h3>Our values</h3><p>Faith, welcome, care for each other and service to our community.</p></div>
    <div class="back__block"><h3>When we meet</h3><p>Sunday worship 11.00am<br>Wednesday prayer 7.30pm<br>Ladies Group 1st Friday</p></div>
    <div class="back__block"><h3>Where we meet</h3><p>14 Example Lane<br>London SE0 0AA</p></div>
    <div class="back__block"><h3>Getting here</h3><p>Buses stop at Example Lane; the station is a 5 minute walk.</p></div>
    <div class="back__block"><h3>Parking</h3><p>Free car park on site, with spaces kept for blue badge holders.</p></div>
    <div class="back__block"><h3>Lantern Nook</h3><p>Our community café, open after Sunday worship.</p></div>
    <div class="back__block"><h3>Follow us</h3><p>www.lanternnook-example.org<br>lantern.nook.uk</p></div>
  </div>
  <p class="back__foot">
    Telephone: +44 (0)20 3000 0123 · E-mail: hello@bwlk-example.org<br>
    Web: www.bwlk-example.org
  </p>
</section>
</body>
</html>
```